Design mobile friendly real estate and property management company landing page

Design a clean, crisp modern looking landing page that is mobile-friendly (must resize, preferably using bootstrap framework). Landing page will consist of heading with login area, company info, body consists of company description and services, a list of available rental properties with photos, and a footer with additional links and info. Working on updating with text for text areas marked A, B, and C on the layout pdf, but in meantime, lorem ipsum is fine. I can connect events to most buttons, etc. Just need the bootstrap and html functionality set up. Previous company website (which should not be relied upon) is www.kbtq.net This is somewhat of a template for a start, but looking for a more professional and modern design for the new website. But this gives an idea of the content and what needs to be displayed, and how.

Target Market(s)

Clients looking for a property management company that is efficient and well-organized.

Industry/Entity Type

Property Management

Coding

Coded - Design and coding required

Number of Pages Required

1 page

Font styles to use
Sans Serif

Colors
0355a3

Requirements
Must have
• Resize for the screen using bootstrap.
• Navigation that collapses for mobile devices
• Large text boxes and good solid spacing around all elements.
Nice to have
• for property images it would be nice if they can be swiped on touch enabled devices (to the next or previous image). And have navigation that can be clicked to next or previous images.
• Would be nice if a captcha verification was included on contact form.
Should not have
• Fancy or eccentric art

```html
<!DOCTYPE html>
<html lang="en">
<head>
<meta charset="utf-8">
<title>Harborline Realty Services</title>
<link href="https://fonts.googleapis.com/css2?family=Roboto+Slab:wght@300;400&family=Roboto:wght@400;500&display=swap" rel="stylesheet">
<style>
:root{
  --navy:#141d33;
  --navy-2:#1a2540;
  --blue:#2a9be0;
  --cyan:#26b6e8;
  --white:#fff;
  --text:#333;
  --pale:#f3f4f6;
}
*{box-sizing:border-box;margin:0;padding:0}
html,body{width:776px;height:1200px;overflow:hidden}
body{position:relative;font-family:"Roboto Slab",serif;font-weight:300;color:var(--text);background:#dfe5ec}
.hero-photo{position:absolute;left:0;top:0;width:776px;height:445px;background:linear-gradient(180deg,#5e8e88 0%,#7aa39b 35%,#3c4b58 70%,#1c1a22 100%)}
.lower-photo{position:absolute;left:0;top:445px;width:776px;height:710px;background:linear-gradient(180deg,#eef1f5 0%,#dfe4ea 45%,#c7ced6 75%,#d5d9dd 100%)}
.brand{position:absolute;left:0;top:6px;width:248px;height:68px;background:var(--white);display:flex;align-items:center;justify-content:center}
.brand-name{font-family:"Roboto Slab",serif;font-weight:400;font-size:15px;color:var(--navy)}
.navbar{position:absolute;left:248px;top:38px;width:528px;height:52px;background:var(--navy);display:flex;align-items:center;padding-left:52px}
.navbar a{font-family:"Roboto",sans-serif;font-size:10px;color:var(--white);text-decoration:none;padding:5px 9px;border-radius:11px}
.navbar a.active{background:var(--blue)}
.welcome{position:absolute;left:52px;top:148px;width:437px;height:202px;background:rgba(255,255,255,.94);padding:18px 20px}
.welcome h1{font-weight:400;font-size:14.5px;color:#222;padding-bottom:7px;border-bottom:1px solid #999;margin-bottom:10px;letter-spacing:.2px}
.welcome p{font-size:7.4px;line-height:14px;margin-bottom:8px;color:#333}
.badges{display:flex;align-items:center;gap:12px;margin-top:12px}
.form-card{position:absolute;left:512px;top:110px;width:212px;height:304px;background:rgba(255,255,255,.96)}
.form-head{background:var(--navy);height:39px;text-align:center;padding-top:6px}
.form-head h2{font-family:"Roboto",sans-serif;font-weight:500;font-size:14px;color:var(--white)}
.form-head p{font-family:"Roboto",sans-serif;font-size:9.5px;color:var(--cyan)}
.field{margin:12px 14px 0;height:28px;border:1px solid #bbb;font-family:"Roboto",sans-serif;font-size:7px;color:#777;padding:9px 9px}
.field.tall{height:45px}
.submit{margin:11px 15px 0;height:28px;background:var(--blue);color:var(--white);font-family:"Roboto",sans-serif;font-weight:500;font-size:11px;display:flex;align-items:center;justify-content:center}
.service{position:absolute;top:486px;width:327px;height:213px;text-align:center;padding-top:40px;color:var(--white)}
.service.pm{left:52px;background:linear-gradient(180deg,#4c5f82 0%,#c78663 45%,#2f2f3a 70%,#161a22 100%)}
.service.re{left:397px;background:linear-gradient(180deg,#142458 0%,#2a3678 40%,#5a4b78 60%,#101830 100%)}
.service h3{font-weight:400;font-size:17px;color:var(--cyan);margin-bottom:10px}
.service p{font-size:7.6px;line-height:14px;padding:0 28px}
.btn-more{display:inline-block;margin-top:20px;background:var(--white);color:#222;font-size:7.6px;padding:6px 12px}
.label{position:absolute;left:52px;width:155px;height:26px;background:var(--navy);color:var(--white);font-weight:400;font-size:11.5px;padding:6px 22px}
.bar{position:absolute;left:224px;width:501px;height:26px;background:var(--blue);color:var(--white);font-weight:400;font-size:9.6px;display:flex;align-items:center;padding-left:22px}
.bar span:last-child{position:absolute;left:286px}
.thumb{position:absolute;left:52px;width:155px;height:131px}
.thumb.rent{top:775px;background:linear-gradient(180deg,#5a86b8 0%,#a69c7c 40%,#8a7c5e 65%,#c9c9c6 100%)}
.thumb.sale{top:984px;background:linear-gradient(180deg,#3c7cc6 0%,#c9a57a 40%,#b78c5e 75%,#8a9a6a 100%)}
.detail{position:absolute;left:224px;width:501px;height:131px;background:linear-gradient(180deg,#141d33,#1b2a44);color:var(--white);font-size:7.6px}
.col{position:absolute;top:34px;line-height:17.4px}
.col b{font-weight:400;color:var(--cyan);font-size:8.6px}
.desc{position:absolute;left:287px;top:31px;width:204px;line-height:13.8px;font-size:7.4px}
.footer{position:absolute;left:0;top:1155px;width:776px;height:45px;background:var(--navy);font-size:7.6px;color:var(--blue)}
.footer span{position:absolute;top:18px}
</style>
</head>
<body>
<div class="hero-photo" role="img" aria-label="Palm trees and a city skyline at dusk across the bay"></div>
<div class="lower-photo" role="img" aria-label="Faded coastal cliffs and beach houses"></div>

<header>
  <div class="brand"><span class="brand-name">Harborline Realty Services</span></div>
  <nav class="navbar">
    <a class="active" href="#">HOME</a><a href="#">ABOUT</a><a href="#">FOR RENT</a><a href="#">FOR SALE</a><a href="#">PROPERTY MANAGEMENT</a><a href="#">REAL ESTATE</a>
  </nav>
</header>

<section class="welcome">
  <h1>WELCOME TO BAYFRONT REALTY &amp; MANAGEMENT</h1>
  <p>We are a locally owned and operated San Diego Property Management company. Serving all areas of San Diego County, we provide personal, reliable property management services for all types of residential property.</p>
  <p>Please give us a call anytime at (555) 210-4470 to discuss your property management needs, or fill out our proposal request form and we will be in touch with you promptly.</p>
  <div class="badges">
    <div style="width:79px;height:30px;background:#1d4f7a"></div>
    <div style="width:62px;height:24px;background:#e7edf3"></div>
    <div style="width:54px;height:32px;background:#eef3e2"></div>
    <div style="width:34px;height:34px;border-radius:50%;background:#dd4b39"></div>
    <div style="width:32px;height:11px;background:#4b8ed1"></div>
    <div style="width:48px;height:46px;background:#e9ecef"></div>
  </div>
</section>

<aside class="form-card">
  <div class="form-head"><h2>HOW CAN I HELP YOU?</h2><p>Tell Us About Your Case</p></div>
  <div class="field">Your Name :</div>
  <div class="field">Your Email :</div>
  <div class="field">Your Contact :</div>
  <div class="field">Subject Property:</div>
  <div class="field tall">Comments :</div>
  <div class="submit">SUBMIT</div>
</aside>

<section class="service pm" role="img" aria-label="Pier at sunset">
  <h3>PROPERTY MANAGEMENT</h3>
  <p>Lorem ipsum dolor sit amet, consectetur adipiscing elit. Morbi eget ante nec velit sagittis porttitor ut cursus est. Maecenas sit amet sagittis sapien, in elementum quam. Maecenas cursus gravida arcu, id congue ligula cursus quis.</p>
  <span class="btn-more">LEARN MORE</span>
</section>
<section class="service re" role="img" aria-label="City skyline at night over the water">
  <h3>REAL ESTATE</h3>
  <p>Lorem ipsum dolor sit amet, consectetur adipiscing elit. Morbi eget ante nec velit sagittis porttitor ut cursus est. Maecenas sit amet sagittis sapien, in elementum quam. Maecenas cursus gravida arcu, id congue ligula cursus quis.</p>
  <span class="btn-more">LEARN MORE</span>
</section>

<div class="label" style="top:738px">FOR RENT</div>
<div class="bar" style="top:738px"><span>2187 MAPLE CREST AVE SAN DIEGO, CA 92104</span><span>2 BEDROOM, 1 BATH CONDO</span></div>
<div class="thumb rent" role="img" aria-label="Condo building with garages and a pickup truck"></div>
<div class="detail" style="top:775px">
  <div class="col" style="left:22px"><b>Rent:</b> $1,600.00<br><b>Available:</b> 6/1/2016<br><b>Sqft:</b> 675<br><b>Lease:</b> 12 Months</div>
  <div class="col" style="left:137px"><b>Community:</b> North Park<br><b>Parking:</b> 2 assigned spaces off-s...<br><b>Pets:</b> Inquire<br><b>Laundry:</b> On-Site</div>
  <div class="desc">Highly upgraded 2BR/1BA condo in gated North Park community. Unit features hardwood flooring, granite counters in kitchen and bathroom, appliances included. Two assigned off-street parking spaces. Must have excellent rental history, sorry, No ...</div>
</div>

<div class="label" style="top:947px">FOR SALE</div>
<div class="bar" style="top:947px"><span>908 VISTA RIDGE LN CHULA VISTA, CA 91915</span><span>3 BEDROOM, 2.5 BATH SINGLE-FAMILY</span></div>
<div class="thumb sale" role="img" aria-label="Three-level detached house with attached garage"></div>
<div class="detail" style="top:984px">
  <div class="col" style="left:22px"><b>Offered At:</b> $465,000.00<br><b>Status:</b> 6/1/2016<br><b>Sqft:</b> 675<br><b>HOA Dues:</b> 12 Months</div>
  <div class="col" style="left:137px"><b>Community:</b> Eastlake<br><b>Parking:</b> 2 car attached garage<br><b>Pets:</b><br><b>Laundry:</b> Laundry Room</div>
  <div class="desc">Recently built tri-level detached home features 2190 sqft, 3 bedrooms plus large bonus room/family room, plus den/office, with 2 car attached garage in gated community. Unit features newer appliances, hardwood flooring downstairs, open kitchen, ...</div>
</div>

<footer class="footer">
  <span style="left:52px">©2016 Harborline Realty Services. All Rights Reserved.</span>
  <span style="left:349px">7320 Harbor View Dr, San Diego, CA 92107</span>
  <span style="left:671px">Privacy Policy</span>
</footer>
</body>
</html>
```